Free offer card

I need a business card sized FREE CLASS offer thing....Our target market is 18-40 year old women. We are the "sexy" pole studio but don't want to scare people off. This card will be given out by students and staff when they meet people that are interested and also put in hair dressers and sports shops etc. I've got HEAPS of photos so I'll upload a few, I'll also upload the last brochure we did but I'm not sure it's really doing it's job....might be a little scary? The free trial class maybe wasn't clear enough. I think maybe free class instead of using the word "trial" so they don't think they are going to get a hard sell. Need a space we can write student/teachers name on it...maybe Marlo's Muse_________
And need both studios details on it (on attached brochure) happy to send different photos if it helps
I can get high res stuff and better copies of the fit fierce sexy brochure if you want...haven't used this website before not really sure what you need

```html
<!DOCTYPE html>
<html lang="en">
<head>
<meta charset="utf-8">
<title>Marlo's Pole Studio – Free Class Card</title>
<link rel="stylesheet" href="https://fonts.googleapis.com/css2?family=Lato:wght@400;700&family=Open+Sans:wght@400;600;700&display=swap">
<style>
  :root {
    --magenta: #d9177e;
    --magenta-dark: #9e0f5b;
    --teal: #00b8b1;
    --teal-dark: #07827e;
    --teal-deep: #0d6f70;
    --ink: #111111;
    --white: #ffffff;
    --stage: #2b211c;
  }
  * { box-sizing: border-box; margin: 0; padding: 0; }
  html, body { width: 1200px; height: 1200px; overflow: hidden; background: var(--stage); }
  .card {
    position: absolute;
    left: 100px;
    width: 1000px;
    height: 546px;
    overflow: hidden;
    background: var(--white);
  }
  .card--front { top: 42px; }
  .card--back { top: 622px; }
  .card__shapes { position: absolute; inset: 0; width: 100%; height: 100%; }
  .photo { position: absolute; top: 0; left: 0; height: 100%; }
  .photo--front {
    width: 560px;
    background:
      radial-gradient(ellipse 45% 55% at 42% 55%, rgba(150, 90, 80, 0.55) 0%, rgba(150, 90, 80, 0) 100%),
      radial-gradient(ellipse at 25% 25%, #2fd3cb 0%, var(--teal) 45%, #00807b 100%);
  }
  .photo--back {
    width: 600px;
    background:
      radial-gradient(ellipse 55% 35% at 48% 38%, rgba(190, 190, 190, 0.5) 0%, rgba(190, 190, 190, 0) 100%),
      radial-gradient(ellipse at 45% 35%, #3b3b3b 0%, #161616 45%, #000 100%);
  }
  .brand {
    position: absolute;
    font-family: "Lato", sans-serif;
    font-weight: 700;
    font-size: 27px;
    line-height: 1;
    white-space: nowrap;
  }
  .brand--front { left: 30px; top: 48px; color: var(--white); }
  .brand--back { left: 745px; top: 38px; transform: translateX(-50%); color: var(--magenta); font-size: 25px; }
  .headline {
    position: absolute;
    left: 548px; top: 60px;
    font-family: "Open Sans", sans-serif;
    font-weight: 700;
    font-size: 66px;
    line-height: 1.1;
    color: var(--white);
    white-space: nowrap;
  }
  .intro {
    position: absolute;
    left: 538px; top: 160px;
    font-family: "Lato", sans-serif;
    font-size: 23.5px;
    line-height: 30.5px;
    color: var(--ink);
    white-space: nowrap;
  }
  .field {
    position: absolute;
    font-family: "Lato", sans-serif;
    font-size: 21px;
    color: var(--ink);
    white-space: nowrap;
  }
  .field--teacher { left: 537px; top: 310px; }
  .field--student { left: 537px; top: 365px; }
  .field--date { left: 537px; top: 420px; }
  .field--place { left: 793px; top: 420px; }
  .web {
    position: absolute;
    left: 554px; top: 510px;
    font-family: "Lato", sans-serif;
    font-size: 18.5px;
    letter-spacing: 2.4px;
    color: var(--white);
    white-space: nowrap;
  }
  .join-title {
    position: absolute;
    left: 752px; top: 112px;
    transform: translateX(-50%);
    font-family: "Open Sans", sans-serif;
    font-weight: 600;
    font-size: 30px;
    color: var(--white);
    white-space: nowrap;
  }
  .join-text {
    position: absolute;
    left: 578px; top: 156px;
    font-family: "Open Sans", sans-serif;
    font-size: 17px;
    line-height: 21.5px;
    color: var(--white);
    white-space: nowrap;
  }
  .contact-title {
    position: absolute;
    left: 755px; top: 294px;
    transform: translateX(-50%);
    font-family: "Open Sans", sans-serif;
    font-weight: 400;
    font-size: 24px;
    color: var(--white);
    white-space: nowrap;
  }
  .studio {
    position: absolute;
    left: 750px;
    transform: translateX(-50%);
    font-family: "Lato", sans-serif;
    font-size: 17.5px;
    line-height: 21.5px;
    color: var(--white);
    text-align: center;
    white-space: nowrap;
    font-style: normal;
  }
  .studio--city { top: 341px; }
  .studio--bayside { top: 429px; }
</style>
</head>
<body>

<section class="card card--front">
  <div class="photo photo--front" role="img" aria-label="Photo of a dancer leaning back from a brass pole in a pink two-piece against a teal backdrop"></div>
  <svg class="card__shapes" viewBox="0 0 1250 682" preserveAspectRatio="none" aria-hidden="true">
    <polygon points="637,0 682,0 667,682 640,682 577,388" fill="var(--teal-deep)"/>
    <polygon points="682,0 1250,0 1250,682 667,682 577,388 640,190" fill="var(--white)"/>
    <polygon points="580,191 603,191 603,213" fill="var(--magenta-dark)"/>
    <polygon points="617,55 1250,55 1250,191 580,191" fill="var(--magenta)"/>
    <polygon points="667,625 1250,625 1250,682 687,682" fill="var(--magenta)"/>
  </svg>
  <div class="brand brand--front">Marlo's Pole Studio</div>
  <h1 class="headline">Free Class !</h1>
  <p class="intro">At Marlo's Pole Studio our classes are<br>designed to suit all types of students,<br>from Beginners to Advanced, industry to<br>non-industry and everyone in between.</p>
  <p class="field field--teacher">Teacher’s Name -</p>
  <p class="field field--student">Student’s Name -</p>
  <p class="field field--date">Date -</p>
  <p class="field field--place">Place -</p>
  <p class="web">WWW.MARLOSPOLESTUDIO.COM.AU</p>
</section>

<section class="card card--back">
  <div class="photo photo--back" role="img" aria-label="Black and white photo of a dancer holding an inverted split on a pole against a dark backdrop"></div>
  <svg class="card__shapes" viewBox="0 0 1250 682" preserveAspectRatio="none" aria-hidden="true">
    <polygon points="606,0 1250,0 1250,682 587,682 703,372" fill="var(--magenta)"/>
    <polygon points="643,0 1250,0 1250,112 661,112" fill="var(--white)"/>
    <polygon points="661,112 1250,112 1250,667 642,667 703,372" fill="var(--teal)"/>
  </svg>
  <div class="brand brand--back">Marlo's Pole Studio</div>
  <h2 class="join-title">COME JOIN US</h2>
  <p class="join-text">Our Beginners, Intermediate and Advanced<br>terms are all across 8 weeks, and consist of a<br>weekly 1 hour session of intense Pole Instruction<br>combined with Dance orientated Warm-up and<br>Cool Down.</p>
  <h3 class="contact-title">Contact Us</h3>
  <address class="studio studio--city">CITY STUDIO<br>Level 2, 118 Harbour Lane, Sydney NSW 2000<br>(02) 9000-1412</address>
  <address class="studio studio--bayside">BAYSIDE STUDIO<br>4/62 Coastline Rd, Bayside NSW 2229<br>(02) 9000-3857<br>info@marlospolestudio.com.au</address>
</section>

</body>
</html>
```